Brochure for services and brand overview of new agency

With the recent launch of a new brand and business strategy agency, I am looking for a 2-3 page digital brochure that I can attach to emails as I open the dialogue with potential clients. This brochure has to fall in line with our brand...modern and sleek, with a highly professional look and feel. The content can come from a combination of our website (www.quillbarn.co) and any additional content can come from you or just ask me to provide. Logos and other materials are provided as well. I have also included a sample of one of my other brochures from another company I own, just so you can get an example of the quality and feel I like.

Target Market(s)

Divorce Professionals (Attorneys, Mediators, Therapists, etc)

Industry/Entity Type

Agency

Font styles to use
Serif

Requirements
Must have
• High end brand feel.
Specific content with relation to services, brand ethos, etc....with a subtle call to action.
Should not have
• Hard Sales Language
Cheap looking stock photos

Don't go too heavy in written content. Just scratch the surface in a way that will capture attention and get them to want to call. It's more about the design and inspirational aspects of it.

```html
<!DOCTYPE html>
<html lang="en">
<head>
<meta charset="utf-8">
<title>Quillbarn Agency Brochure</title>
<link href="https://fonts.googleapis.com/css2?family=Montserrat:wght@300;400;600;700&family=Open+Sans:wght@400;600&display=swap" rel="stylesheet">
<style>
:root{
  --red:#c8102e;
  --ink:#1d1d1f;
  --dark:#141416;
  --grey:#6b6b70;
  --paper:#ffffff;
  --stage:#e9e9eb;
}
*{margin:0;padding:0;box-sizing:border-box}
html,body{width:1200px;height:2196px;overflow:hidden;background:var(--stage)}
body{position:relative;font-family:"Open Sans",Arial,sans-serif;color:var(--ink)}
.page{position:absolute;width:524px;height:680px;background:var(--paper);overflow:hidden;box-shadow:0 2px 8px rgba(0,0,0,.18)}
.cover{left:48px;top:40px}
.about{left:628px;top:40px}
.services{left:48px;top:772px}
.hire{left:628px;top:772px}
.back{left:338px;top:1512px}
.photo{position:absolute}
.h-title{font-family:"Montserrat",Arial,sans-serif;font-weight:300;text-transform:uppercase;letter-spacing:1px;line-height:1.05}
.body-text{font-size:7px;line-height:1.55;color:var(--grey)}
.footer{position:absolute;left:0;bottom:0;width:100%;height:30px;background:var(--dark);color:#fff;font-family:"Montserrat",Arial,sans-serif;font-size:9px;letter-spacing:4px;text-align:center;line-height:30px}
.footer.light{background:none;color:var(--ink)}
.footer-mark{position:absolute;right:16px;bottom:6px;width:18px;height:18px;border-radius:50%;background:var(--red)}
.brand{display:flex;align-items:center;gap:10px;font-family:"Montserrat",Arial,sans-serif;font-weight:700}
.brand-dot{border-radius:50%;background:var(--red);flex:none}
.label{font-family:"Montserrat",Arial,sans-serif;font-weight:700;font-size:7.5px;text-transform:uppercase;letter-spacing:.5px;color:var(--ink);margin-bottom:5px}
/* cover */
.cover .photo{inset:0;background:linear-gradient(160deg,#4a4f57 0%,#2b2f35 45%,#17191c 100%)}
.cover .h-title{position:absolute;left:26px;top:30px;width:380px;color:#fff;font-size:27px}
.cover-band{position:absolute;left:0;top:470px;width:330px;height:70px;background:#fff;display:flex;align-items:center;padding-left:30px}
.cover-band .brand{font-size:26px;color:var(--ink)}
.cover-url{position:absolute;left:40px;top:552px;color:#fff;font-family:"Montserrat",Arial,sans-serif;font-size:8px;letter-spacing:4px}
/* about */
.about .photo{left:250px;top:0;width:274px;height:215px;background:linear-gradient(135deg,#8a8f96,#3e434a)}
.about-head{position:absolute;left:20px;top:22px;padding:12px 14px;border-left:4px solid var(--red);background:#fff;z-index:1}
.about-head .h-title{font-size:30px;color:var(--ink)}
.about-copy{position:absolute;left:24px;top:130px;width:215px}
.about-copy p{margin-bottom:8px}
.about-quote{position:absolute;left:272px;top:250px;width:220px;font-size:9px;line-height:1.45;color:var(--ink);font-weight:600;border-left:3px solid var(--red);padding-left:10px}
.about-list{position:absolute;left:272px;top:330px;width:220px;font-family:"Montserrat",Arial,sans-serif;font-size:7.5px;font-weight:700;line-height:1.6;color:var(--red);text-transform:uppercase}
/* services */
.services .h-title{position:absolute;left:24px;top:26px;font-size:30px;color:var(--ink)}
.services-rule{position:absolute;left:24px;top:64px;width:476px;height:2px;background:var(--red)}
.services-lead{position:absolute;left:24px;top:72px;width:476px;font-size:8px;color:var(--red);font-weight:600}
.service{position:absolute;left:24px;width:476px;display:flex;gap:18px;align-items:flex-start}
.service .photo{position:relative;width:200px;height:118px;flex:none}
.service .copy{flex:1;padding-top:6px}
.s1{top:112px}.s1 .photo{background:linear-gradient(135deg,#3a3a3d,#0f0f10)}
.s2{top:290px}.s2 .photo{background:linear-gradient(135deg,#d8d8d8,#9a9ea4)}
.s3{top:450px}.s3 .photo{background:linear-gradient(135deg,#6d8fa8,#c9a77e)}
/* hire */
.hire .h-title{position:absolute;left:24px;top:26px;font-size:30px;color:var(--red)}
.hire-rule{position:absolute;left:24px;top:64px;width:476px;height:2px;background:var(--red)}
.hire .photo{left:24px;top:80px;width:476px;height:240px;background:linear-gradient(120deg,#c9ccd1,#6f7780 60%,#3b4047)}
.hire-pitch{position:absolute;left:36px;top:92px;width:220px;padding:14px;background:rgba(20,20,22,.88);color:#fff;font-family:"Montserrat",Arial,sans-serif;font-size:8.5px;font-weight:600;line-height:1.45;text-transform:uppercase}
.hire-cols{position:absolute;left:24px;top:342px;width:476px;display:grid;grid-template-columns:repeat(5,1fr);gap:12px}
/* back */
.back{background:var(--dark)}
.back .photo{inset:0;background:radial-gradient(ellipse at 50% 45%,#2e3034 0%,#141416 70%)}
.back-brand{position:absolute;left:0;top:270px;width:100%;justify-content:center;font-size:24px;color:#fff}
.back-contact{position:absolute;left:110px;top:560px;width:320px;display:flex;gap:40px;border-left:3px solid var(--red);padding-left:12px;font-size:7px;line-height:1.7;color:#d6d6d8}
</style>
</head>
<body>

<section class="page cover">
  <div class="photo" role="img" aria-label="Dim office photo of a team meeting around a table"></div>
  <h1 class="h-title">With a passion matched only by that of our clients</h1>
  <div class="cover-band"><div class="brand">Quillbarn</div></div>
  <div class="cover-url">www.quillbarn.co</div>
</section>

<section class="page about">
  <div class="photo" role="img" aria-label="Photo of colleagues working together in a bright office"></div>
  <div class="about-head"><h2 class="h-title">About<br>Quillbarn</h2></div>
  <div class="about-copy body-text">
    <p>Our founder built Quillbarn on a simple belief: every practice deserves a brand as thoughtful as the care it gives. We listen first, then shape a clear story that people trust and remember.</p>
    <p>Our team brings strategy, design and digital craft together under one roof, so each decision supports the next. Nothing is rushed, nothing is generic, and every detail is made to fit the way you work.</p>
    <p>We partner with attorneys, mediators and therapists who guide families through change. Their work calls for calm, clarity and warmth, and their brand should reflect all three at every touchpoint.</p>
    <p>From first idea to final launch, we stay close, measure what matters and refine as you grow. The result is a presence that feels honest, modern and entirely your own.</p>
  </div>
  <div class="about-quote">With a passion matched only by that of our clients, Quillbarn is committed to creating new opportunities and rebuilding brands.</div>
  <div class="about-list">Optimization / Building / Strategic Marketing / Consultation / Brand Management / Global Brand Recognition / Operational Growth / Strategy / Social Media</div>
  <div class="footer">www.quillbarn.co</div>
  <div class="footer-mark"></div>
</section>

<section class="page services">
  <h2 class="h-title">Our Services</h2>
  <div class="services-rule"></div>
  <p class="services-lead">We offer full service representation to give your practice a voice that carries.</p>
  <div class="service s1">
    <div class="photo" role="img" aria-label="Dark photo of a person working in low light"></div>
    <div class="copy body-text"><div class="label">Complete Brand Experience</div>A full review of how your practice is seen today, followed by a clear plan and a refreshed identity that speaks to the clients you want to serve.</div>
  </div>
  <div class="service s2">
    <div class="copy body-text"><div class="label">Custom Brand Experience</div>Choose only the pieces you need, from naming and messaging to a new website, and we shape each one to sit naturally with what already works.</div>
    <div class="photo" role="img" aria-label="Photo of hands holding a phone"></div>
  </div>
  <div class="service s3">
    <div class="photo" role="img" aria-label="Photo of a smiling group outdoors"></div>
    <div class="copy body-text"><div class="label">Innovation Outsource Group</div>Ongoing creative support on call, giving your team steady access to strategy, content and design whenever new ideas need a home.</div>
  </div>
  <div class="footer light">www.quillbarn.co</div>
  <div class="footer-mark"></div>
</section>

<section class="page hire">
  <h2 class="h-title">Hire Adrian</h2>
  <div class="hire-rule"></div>
  <div class="photo" role="img" aria-label="Photo of the founder seated at a desk"></div>
  <div class="hire-pitch">Book Adrian for a session on the ideas that build lasting brands, clear strategy and client trust in changing times.</div>
  <div class="hire-cols body-text">
    <div><div class="label">Keynotes</div>Talks that leave rooms inspired, with plain lessons drawn from years of building brands.</div>
    <div><div class="label">Workshops</div>Hands on sessions that help teams find their voice and shape a clear message.</div>
    <div><div class="label">Coaching</div>One to one guidance for leaders ready to grow their practice with purpose.</div>
    <div><div class="label">Panels</div>A calm and candid voice on brand, growth and the future of service.</div>
    <div><div class="label">Retreats</div>Quiet days away to reset priorities and plan the next chapter.</div>
  </div>
  <div class="footer light">www.quillbarn.co</div>
  <div class="footer-mark"></div>
</section>

<section class="page back">
  <div class="photo" role="img" aria-label="Dark photo of a person walking through a city"></div>
  <div class="brand back-brand"><span class="brand-dot" style="width:22px;height:22px"></span>Quillbarn</div>
  <div class="back-contact">
    <div>120 Harbour Lane<br>Suite 400<br>Lakeview, ON</div>
    <div>555 014 2280<br>hello@quillbarn.co</div>
  </div>
</section>

</body>
</html>
```